Design an infographic based off our 7 stats

Design a infographic based on our previous infographic style (see attachment).

The image should be long and thin, similar dimensions to the previous infographic.

The 7 stats below should be displayed. Some stats have a second percentage, these should be shown in the same line of next.

Each stat should have an icon/picture as explained below.

Small text in grey at the bottom:
"For more details: https://www.velmarock.com/blog/quirky-crypto-survey"

See attachments for a suggested draft format. Feel free to use your own design if you think there are better ways to display this data.

Note: the percentages and text are not final.

Stat #1
Icon/picture: bitcoin
Figure: 65%
Text: may buy crypto in the next 12 months

Stat #2
Icon/picture: clock
Figure: 63%
Text: it's a good time to buy now or when the price drops slightly

Stat #3
Icon/picture: fire
Figure: 70%
Text: media gets too caught up in hype when things run hot

Stat #4
Icon/picture: bars of gold
Figure: 61%
Text: investment properties and gold are good supplementary investments

Stat #5
Icon/picture: shield
Figure: 44%
Text: play it careful and conservatively or scared of missing out

Stat #6
Icon/picture: gas pump
Figure: 55%
Text: want to use crypo in their everyday

Stat #7
Icon/picture: rocket and moon
Figure: 84%
Text: bitcoin will be $10-50k or more in 10 years

Font styles to use
Other font styles liked:
• See previous infographic attached

Colors

Designer to choose colors to be used in the design.

Requirements
Must have
• Velmarock logo
• 7 stats with icon, percentage and text
• Same color theme as Velmarock brand
Nice to have
• Same style as the previous inforgraphic (see attachement)

```html
<!DOCTYPE html>
<html lang="en">
<head>
<meta charset="utf-8">
<title>Velmarock – Quirky Crypto Survey</title>
<link href="https://fonts.googleapis.com/css2?family=Bebas+Neue&family=Oswald:wght@400;500&display=swap" rel="stylesheet">
<style>
  :root {
    --bg-green: #7db43c;
    --card-white: #ffffff;
    --text-grey: #555555;
    --footer-green: #4e6e2a;
    --blue: #1db6e2;
    --teal: #1fcf9e;
    --periwinkle: #9fb4f6;
    --orange: #f15b2c;
    --coin-gold: #f7a823;
    --coin-orange: #f28a1e;
  }
  * { box-sizing: border-box; margin: 0; padding: 0; }
  html, body { width: 1200px; height: 2319px; overflow: hidden; }
  body {
    background: var(--bg-green);
    font-family: "Oswald", "Arial Narrow", sans-serif;
    position: relative;
  }
  .header-coins {
    position: absolute;
    top: 66px;
    width: 340px;
    height: 136px;
    border-radius: 68px;
    background: radial-gradient(circle at 50% 50%, var(--coin-gold), var(--coin-orange) 60%, rgba(242,138,30,0) 75%);
    opacity: .85;
  }
  .header-coins.left { left: 50px; }
  .header-coins.right { right: 50px; }
  .brand {
    position: absolute;
    top: 62px;
    left: 0;
    width: 100%;
    text-align: center;
    color: #fff;
    font-weight: 500;
    font-size: 92px;
    line-height: 110px;
    letter-spacing: 1px;
  }
  .brand-dot {
    display: inline-block;
    width: 22px; height: 22px;
    background: #fff;
    border-radius: 50%;
    vertical-align: middle;
    margin-right: 14px;
    position: relative; top: -6px;
  }
  .survey-banner {
    position: absolute;
    left: 70px; top: 243px;
    width: 1059px; height: 76px;
    background: var(--card-white);
    border-radius: 24px;
    text-align: center;
    color: var(--text-grey);
    font-size: 40px;
    line-height: 76px;
    letter-spacing: 1.5px;
  }
  .stat {
    position: absolute;
    left: 70px;
    width: 1059px;
    height: 237px;
    border-radius: 24px;
    background: var(--card-white);
    overflow: hidden;
  }
  .stat-panel {
    position: absolute;
    top: 0; width: 526px; height: 100%;
    background: var(--panel);
  }
  .stat.panel-left .stat-panel { left: 0; }
  .stat.panel-right .stat-panel { right: 0; }
  .stat-pointer {
    position: absolute;
    top: 50%;
    width: 0; height: 0;
    border-top: 16px solid transparent;
    border-bottom: 16px solid transparent;
    margin-top: -16px;
  }
  .stat.panel-left .stat-pointer { left: 526px; border-left: 16px solid var(--panel); }
  .stat.panel-right .stat-pointer { right: 526px; border-right: 16px solid var(--panel); }
  .stat-icon {
    position: absolute;
    top: 34px;
    height: 170px;
    border-radius: 20px;
    background: var(--icon-fill);
  }
  .stat.panel-left .stat-icon { left: 39px; width: 250px; }
  .stat.panel-right .stat-icon { left: 782px; width: 240px; }
  .stat-figure {
    position: absolute;
    top: 0; height: 100%;
    color: #fff;
    font-family: "Bebas Neue", "Oswald", sans-serif;
    font-size: 150px;
    line-height: 250px;
    text-shadow: 4px 4px 0 rgba(0,0,0,.12);
  }
  .stat.panel-left .stat-figure { left: 304px; }
  .stat.panel-right .stat-figure { left: 570px; }
  .stat-text {
    position: absolute;
    top: 0; height: 100%;
    width: 533px;
    display: flex; align-items: center; justify-content: center;
    text-align: center;
    color: var(--text-grey);
    font-size: 43px;
    line-height: 64px;
    text-transform: uppercase;
    letter-spacing: 1px;
  }
  .stat.panel-left .stat-text { right: 0; }
  .stat.panel-right .stat-text { left: 0; }
  .footer-note {
    position: absolute;
    left: 0; top: 2260px;
    width: 100%;
    text-align: center;
    color: var(--footer-green);
    font-size: 29px;
    letter-spacing: .5px;
    text-transform: uppercase;
  }
</style>
</head>
<body>
  <div class="header-coins left" role="img" aria-label="Scattered gold bitcoin coins with sparkles"></div>
  <div class="header-coins right" role="img" aria-label="Scattered gold bitcoin coins with sparkles"></div>
  <div class="brand"><span class="brand-dot"></span>Velmarock</div>

  <div class="survey-banner">WE SURVEYED OVER 2,600 AUSTRALIANS</div>

  <section class="stat panel-left" style="top:354px; --panel: var(--blue); --icon-fill: linear-gradient(135deg,#b5651d,#f7a823);">
    <div class="stat-panel"></div><div class="stat-pointer"></div>
    <div class="stat-icon" role="img" aria-label="Money bag with stacks of bitcoin coins"></div>
    <div class="stat-figure">65%</div>
    <div class="stat-text">Coinsidering<br>buying crypto in the<br>next 12 months</div>
  </section>

  <section class="stat panel-right" style="top:628px; --panel: var(--teal); --icon-fill: linear-gradient(135deg,#e85a5a,#f4f4f4);">
    <div class="stat-panel"></div><div class="stat-pointer"></div>
    <div class="stat-icon" role="img" aria-label="Ringing red alarm clock"></div>
    <div class="stat-figure">63%</div>
    <div class="stat-text">It's a good time to buy<br>now or when the price<br>drops slightly</div>
  </section>

  <section class="stat panel-left" style="top:902px; --panel: var(--periwinkle); --icon-fill: linear-gradient(180deg,#f7c12a,#ef4b23);">
    <div class="stat-panel"></div><div class="stat-pointer"></div>
    <div class="stat-icon" role="img" aria-label="Orange and yellow flame"></div>
    <div class="stat-figure">70%</div>
    <div class="stat-text">Media gets too<br>caught up in hype<br>when things run hot</div>
  </section>

  <section class="stat panel-right" style="top:1176px; --panel: var(--orange); --icon-fill: linear-gradient(135deg,#f3d9a6,#f7c21f);">
    <div class="stat-panel"></div><div class="stat-pointer"></div>
    <div class="stat-icon" role="img" aria-label="Money bag with dollar sign beside gold bars"></div>
    <div class="stat-figure">61%</div>
    <div class="stat-text">Investment properties<br>and gold are good<br>supplementary investments</div>
  </section>

  <section class="stat panel-left" style="top:1451px; --panel: var(--blue); --icon-fill: linear-gradient(135deg,#e8452c,#6cbf5a);">
    <div class="stat-panel"></div><div class="stat-pointer"></div>
    <div class="stat-icon" role="img" aria-label="Red shield in front of banknotes and coin stacks"></div>
    <div class="stat-figure">44%</div>
    <div class="stat-text">Play it careful and<br>conservatively or<br>scared of missing out</div>
  </section>

  <section class="stat panel-right" style="top:1725px; --panel: var(--teal); --icon-fill: linear-gradient(135deg,#f15b2c,#d63a2a);">
    <div class="stat-panel"></div><div class="stat-pointer"></div>
    <div class="stat-icon" role="img" aria-label="Red and orange fuel pump"></div>
    <div class="stat-figure">55%</div>
    <div class="stat-text">Want to use crypo<br>in their everyday</div>
  </section>

  <section class="stat panel-left" style="top:2000px; --panel: var(--periwinkle); --icon-fill: linear-gradient(135deg,#f3efc8,#ffffff);">
    <div class="stat-panel"></div><div class="stat-pointer"></div>
    <div class="stat-icon" role="img" aria-label="Rocket launching past the moon and clouds"></div>
    <div class="stat-figure">84%</div>
    <div class="stat-text">Bitcoin will be<br>$10K-50K or more<br>in 10 years</div>
  </section>

  <p class="footer-note">For more details: https://www.velmarock.com/blog/quirky-crypto-survey</p>
</body>
</html>
```